Double sided business Card voor Luchtkoel Brederwijk

Card design must be in line with our logo. Clean and professional look. Colors can be used, but not too wild.
Logo in frontside. Details on the backside. We want a qr in the design.

Details: (person)
name: Maarten Bosveld
tel: 06-48271935
maarten@luchtkoelbrederwijk.nl

tel: 088-5063918 (business general)
info@luchtkoelbrederwijk.nl

.

```html
<!DOCTYPE html>
<html lang="nl">
<head>
<meta charset="utf-8">
<title>Luchtkoel Brederwijk – visitekaartje</title>
<link href="https://fonts.googleapis.com/css2?family=Inter:wght@400;500;700&display=swap" rel="stylesheet">
<style>
  :root {
    --brand-blue: #0a63b4;
    --brand-red: #e3111b;
    --card-white: #f1f1f0;
    --text-dark: #3a3a3a;
    --qr-frame: #c9ccd1;
    --backdrop: #d9d4cd;
  }
  * { margin: 0; padding: 0; box-sizing: border-box; }
  html, body {
    width: 1200px; height: 957px; overflow: hidden;
    background: var(--backdrop);
    font-family: "Inter", Arial, sans-serif;
  }
  .canvas { position: relative; width: 1200px; height: 957px; }

  .card {
    position: absolute; left: 289px; width: 620px; height: 355px;
    box-shadow: 0 2px 6px rgba(0,0,0,0.25);
    overflow: hidden;
  }
  .card--front { top: 97px; background: var(--brand-blue); }
  .card--back { top: 495px; background: var(--card-white); }

  /* front */
  .front-brand {
    position: absolute; left: 0; right: 0; top: 78px;
    display: flex; flex-direction: column; align-items: center;
    color: #fff;
  }
  .front-brand__mark {
    width: 96px; height: 96px; border-radius: 50%;
    background: #fff; margin-bottom: 34px;
  }
  .front-brand__name {
    font-weight: 400; font-size: 27px; letter-spacing: 5px;
    line-height: 36px; text-align: center; text-transform: uppercase;
  }

  /* back */
  .back-brand {
    position: absolute; left: 64px; width: 240px; top: 110px;
    display: flex; flex-direction: column; align-items: center;
    color: var(--text-dark);
  }
  .back-brand__mark {
    width: 62px; height: 62px; border-radius: 50%;
    background: var(--brand-blue); margin-bottom: 22px;
  }
  .back-brand__name {
    font-weight: 400; font-size: 17px; letter-spacing: 3.2px;
    line-height: 23px; text-align: center; text-transform: uppercase;
  }
  .divider {
    position: absolute; left: 310px; top: 101px;
    width: 1.5px; height: 153px; background: var(--brand-red);
  }
  .contact { position: absolute; left: 335px; top: 100px; }
  .contact__name {
    font-weight: 700; font-size: 25px; color: var(--brand-blue);
    letter-spacing: -0.5px; line-height: 30px;
  }
  .contact__role {
    font-size: 13.5px; color: var(--brand-red); margin-top: 1px;
  }
  .contact__list { list-style: none; margin-top: 20px; }
  .contact__list + .contact__list { margin-top: 12px; }
  .contact__item {
    display: flex; align-items: center; gap: 8px;
    font-size: 13.5px; color: var(--text-dark); line-height: 20px;
  }
  .contact__item svg { width: 12px; height: 12px; flex: none; }

  .qr-slot {
    position: absolute; right: 26px; top: 26px;
    width: 58px; height: 58px;
    background: #fff; border: 1.5px solid var(--qr-frame);
    border-radius: 3px;
  }

  .footer-rule {
    position: absolute; left: 0; right: 0; top: 315px;
    height: 2px; background: var(--brand-red);
  }
  .footer-band {
    position: absolute; left: 0; right: 0; top: 321px; height: 34px;
    background: var(--brand-blue); color: #fff;
    display: flex; align-items: center; justify-content: center;
    font-size: 13.5px;
  }
</style>
</head>
<body>
<div class="canvas">

  <section class="card card--front" aria-label="Voorkant">
    <div class="front-brand">
      <div class="front-brand__mark"></div>
      <p class="front-brand__name">Luchtkoel<br>Brederwijk</p>
    </div>
  </section>

  <section class="card card--back" aria-label="Achterkant">
    <div class="qr-slot" role="img" aria-label="Plaats voor QR-code naar www.luchtkoelbrederwijk.nl"></div>

    <div class="back-brand">
      <div class="back-brand__mark"></div>
      <p class="back-brand__name">Luchtkoel<br>Brederwijk</p>
    </div>

    <div class="divider"></div>

    <div class="contact">
      <h1 class="contact__name">Maarten Bosveld</h1>
      <p class="contact__role">Founder &amp; CEO</p>

      <ul class="contact__list">
        <li class="contact__item">
          <svg viewBox="0 0 12 12"><path fill="var(--brand-red)" d="M2.4 1l1.8 2.2-1 1.1c.7 1.5 1.9 2.7 3.5 3.5l1.1-1L10 8.6 9 10.5C5 10.3 1.7 7 1.5 3z"/></svg>
          06-48271935
        </li>
        <li class="contact__item">
          <svg viewBox="0 0 12 12"><rect x="0.5" y="2" width="11" height="8" fill="var(--brand-red)"/><path d="M0.8 2.4L6 6.5l5.2-4.1" fill="none" stroke="#fff" stroke-width="1"/></svg>
          maarten@luchtkoelbrederwijk.nl
        </li>
      </ul>
      <ul class="contact__list">
        <li class="contact__item">
          <svg viewBox="0 0 12 12"><path fill="var(--brand-red)" d="M2.4 1l1.8 2.2-1 1.1c.7 1.5 1.9 2.7 3.5 3.5l1.1-1L10 8.6 9 10.5C5 10.3 1.7 7 1.5 3z"/></svg>
          088-5063918 (business general)
        </li>
        <li class="contact__item">
          <svg viewBox="0 0 12 12"><rect x="0.5" y="2" width="11" height="8" fill="var(--brand-red)"/><path d="M0.8 2.4L6 6.5l5.2-4.1" fill="none" stroke="#fff" stroke-width="1"/></svg>
          info@luchtkoelbrederwijk.nl
        </li>
      </ul>
    </div>

    <div class="footer-rule"></div>
    <div class="footer-band">www.luchtkoelbrederwijk.nl</div>
  </section>

</div>
</body>
</html>
```